Medtech Advisory- Brixholm Equity Associates Website

We need a company website, programmed in Typo3.
The design should be clean, modern and simple based on the color and style of our logo.
Brixholm Equity Associates is a Swiss company which assists international medtech companies in relocating all or part of their business to Switzerland.
The site should consist of the following pages: Home, Offering, Customers, Team, Contact us (see also attached pdf file).
Target Market(s)
Medtech Start-ups
Industry/Entity Type
It Company
Coding
Coded - Design and coding required
Requirements
Must have
- Use of the logo provided
- page structure as described above
- programmed in Typo3 so that we can edit ourselves
- responsive for use with mobile devices
Nice to have
- eye catcher to attract readers interest, e.g. visuals

```html
<!DOCTYPE html>
<html lang="en">
<head>
<meta charset="utf-8">
<title>Brixholm Equity Associates</title>
<link href="https://fonts.googleapis.com/css2?family=Jost:wght@400;500&family=Open+Sans:wght@400;600&display=swap" rel="stylesheet">
<style>
:root{
  --blue:#1f5aa6;
  --blue-dark:#124a92;
  --ink:#2a2a2a;
  --text:#444;
  --muted:#6d6d6d;
  --grey-bg:#ececec;
  --line:#dcdcdc;
  --footer:#1e1e1e;
  --footer-bottom:#141414;
  --footer-text:#c9c9c9;
  --social:#2a6fc4;
  --white:#fff;
}
*{box-sizing:border-box;margin:0;padding:0}
html,body{width:1200px;height:2579px;overflow:hidden}
body{position:relative;background:var(--white);font-family:"Open Sans",Arial,sans-serif;color:var(--text)}
h2.section-title{position:absolute;left:0;width:1200px;text-align:center;font-family:"Jost",Arial,sans-serif;font-weight:400;font-size:32px;color:var(--ink)}
h2.section-title span{color:var(--blue)}
h2.section-title::after{content:"";display:block;width:44px;height:3px;background:var(--blue);margin:12px auto 0}

/* header */
.site-header{position:absolute;left:0;top:0;width:1200px;height:120px;background:var(--white)}
.brand{position:absolute;left:98px;top:36px;display:flex;align-items:center;gap:12px;font-family:"Jost",Arial,sans-serif;font-size:27px;color:var(--blue);font-weight:400}
.brand-dot{width:30px;height:30px;border-radius:50%;background:var(--blue)}
.top-contact{position:absolute;top:20px;display:flex;align-items:center;gap:12px;font-family:"Jost",Arial,sans-serif;font-size:20px;color:var(--ink)}
.top-contact .icon{width:32px;height:32px;background:var(--blue);display:flex;align-items:center;justify-content:center}
.main-nav{position:absolute;top:86px;left:590px;font-family:"Jost",Arial,sans-serif;font-size:16px;color:var(--ink)}
.main-nav a{color:inherit;text-decoration:none;position:absolute;white-space:nowrap;transform:translateX(-50%)}
.main-nav a.active{color:var(--blue)}
.main-nav a.active::after{content:"";display:block;height:2px;background:var(--blue);margin-top:6px}
.nav-sep{position:absolute;top:9px;width:3px;height:3px;border-radius:50%;background:#aaa}

/* hero */
.hero{position:absolute;left:0;top:120px;width:1200px;height:521px;background:linear-gradient(180deg,#5b5d63 0%,#7d7467 45%,#3a3836 75%,#d8d4cf 100%)}
.hero-caption{position:absolute;left:0;top:312px;width:1200px;text-align:center;font-family:"Jost",Arial,sans-serif;font-size:36px;color:var(--white);text-shadow:0 2px 6px rgba(0,0,0,.5)}
.hero-arrow{position:absolute;top:245px}
.hero-dots{position:absolute;top:457px;left:566px;display:flex;gap:10px}
.hero-dots i{width:9px;height:9px;border-radius:50%;background:rgba(255,255,255,.5)}
.hero-dots i.on{background:var(--blue-dark);box-shadow:0 0 0 2px #fff}

/* welcome */
.welcome-title{position:absolute;left:98px;top:686px;font-family:"Jost",Arial,sans-serif;font-weight:400;font-size:31px;color:var(--ink)}
.welcome-title span{color:var(--blue)}
.welcome-title::after{content:"";display:block;width:44px;height:3px;background:var(--blue);margin-top:8px}
.welcome-text{position:absolute;left:98px;top:748px;width:564px;font-size:12.6px;line-height:24.5px;text-align:justify;color:var(--text)}
.btn{position:absolute;background:var(--blue);color:var(--white);font-size:13px;font-family:"Open Sans",Arial,sans-serif;display:flex;align-items:center;justify-content:center}
.video-frame{position:absolute;left:701px;top:694px;width:400px;height:251px;border:5px solid #e4e4e4;box-shadow:0 8px 14px rgba(0,0,0,.2)}
.video-still{width:100%;height:100%;background:linear-gradient(135deg,#c8c2b8,#eef0f2 55%,#7e8fa8)}
.play{position:absolute;left:166px;top:96px;width:56px;height:56px;border-radius:50%;background:rgba(255,255,255,.85);border:2px solid var(--blue);display:flex;align-items:center;justify-content:center;padding-left:4px}

/* who */
.who{position:absolute;left:0;top:1004px;width:1200px;height:345px;background:var(--grey-bg)}
.who-card{position:absolute;top:124px;width:332px;height:177px;background:var(--white)}
.who-card h3{position:absolute;left:52px;top:20px;font-family:"Jost",Arial,sans-serif;font-weight:400;font-size:19px;color:var(--ink)}
.who-card p{position:absolute;left:52px;top:62px;width:260px;font-size:12px;line-height:24px;color:var(--blue-dark)}
.corner{position:absolute;right:0;bottom:0;width:0;height:0;border-left:30px solid transparent;border-bottom:30px solid var(--blue)}
.corner-plus{position:absolute;right:4px;bottom:1px;color:#fff;font-size:13px;font-weight:600}
.who-badge{position:absolute;top:150px;width:118px;height:118px;border-radius:50%;background:var(--white);box-shadow:0 2px 8px rgba(0,0,0,.15);display:flex;align-items:center;justify-content:center}
.who-badge .ring{width:102px;height:102px;border-radius:50%;border:3px solid var(--blue);display:flex;align-items:center;justify-content:center}

/* services */
.service-card{position:absolute;top:1482px;width:317px;height:251px;border:1px solid var(--line);background:var(--white);padding:4px}
.service-card .photo{height:186px}
.service-card h3{text-align:center;font-family:"Jost",Arial,sans-serif;font-weight:400;font-size:18px;color:var(--ink);margin-top:18px}

/* team */
.team{position:absolute;left:0;top:1779px;width:1200px;height:470px;background:var(--grey-bg)}
.member{position:absolute;top:119px;width:230px;height:306px;background:var(--white);border-bottom:3px solid var(--blue)}
.member .photo{height:168px}
.member h3{text-align:center;font-family:"Jost",Arial,sans-serif;font-weight:400;font-size:16px;color:var(--ink);margin-top:18px}
.member h3::after{content:"";display:block;width:30px;height:1px;background:var(--line);margin:9px auto 0}
.member p{text-align:center;font-size:12px;line-height:21px;color:var(--text);margin-top:8px;padding:0 10px}
.member .more{position:absolute;left:175px;bottom:-3px;width:44px;height:22px;border-radius:22px 22px 0 0;background:var(--blue);display:flex;justify-content:center;padding-top:5px}
.team-arrow{position:absolute;top:2046px}

/* footer */
.site-footer{position:absolute;left:0;top:2249px;width:1200px;height:281px;background:var(--footer);color:var(--footer-text);font-size:13px}
.footer-col{position:absolute;top:38px}
.footer-col h4{font-family:"Jost",Arial,sans-serif;font-weight:400;font-size:15.5px;color:var(--white);padding-bottom:10px;border-bottom:1px solid #3a3a3a}
.quick-links li{list-style:none;margin-top:16px;font-size:13.5px}
.quick-links li::before{content:"›";margin-right:6px;color:#999}
.contact-line{display:flex;gap:12px;margin-top:14px;line-height:22px}
.field{background:#3a3a3a;height:34px;margin-top:4px;padding:8px 10px;font-size:11px;color:#bbb}
.field.big{height:54px}
.social{position:absolute;top:212px;left:940px;display:flex;gap:14px}
.social i{width:28px;height:28px;border-radius:50%;background:var(--social);display:block}
.footer-bottom{position:absolute;left:0;top:2530px;width:1200px;height:49px;background:var(--footer-bottom);color:var(--footer-text);font-size:13px;display:flex;align-items:center;justify-content:center}
</style>
</head>
<body>

<header class="site-header">
  <div class="brand"><span class="brand-dot"></span>Brixholm Equity Associates</div>
  <div class="top-contact" style="left:670px">
    <span class="icon"><svg width="16" height="16" viewBox="0 0 24 24"><path fill="#fff" d="M6.6 10.8c1.4 2.8 3.8 5.1 6.6 6.6l2.2-2.2c.3-.3.7-.4 1-.2 1.1.4 2.3.6 3.6.6.6 0 1 .4 1 1V20c0 .6-.4 1-1 1C10.6 21 3 13.4 3 4c0-.6.4-1 1-1h3.5c.6 0 1 .4 1 1 0 1.3.2 2.5.6 3.6.1.3 0 .7-.2 1l-2.3 2.2z"/></svg></span>
    (123) 555 0190
  </div>
  <div class="top-contact" style="left:896px;font-size:17px">
    <span class="icon"><svg width="16" height="12" viewBox="0 0 16 12"><rect width="16" height="12" fill="#fff"/><path d="M0 0l8 6 8-6" stroke="#1f5aa6" stroke-width="1.5" fill="none"/></svg></span>
    info@brixholm-equity.com
  </div>
  <nav class="main-nav">
    <a class="active" style="left:24px">Home</a>
    <span class="nav-sep" style="left:72px"></span>
    <a style="left:129px">Offering</a>
    <span class="nav-sep" style="left:186px"></span>
    <a style="left:247px">Customers</a>
    <span class="nav-sep" style="left:301px"></span>
    <a style="left:357px">Team</a>
    <span class="nav-sep" style="left:407px"></span>
    <a style="left:471px">Contact Us</a>
  </nav>
</header>

<section class="hero" role="img" aria-label="Business people in silhouette meeting in a bright office with a city skyline behind">
  <svg class="hero-arrow" style="left:58px" width="22" height="56" viewBox="0 0 22 56"><path d="M20 2L2 28l18 26" stroke="#fff" stroke-width="2" fill="none" opacity=".8"/></svg>
  <svg class="hero-arrow" style="left:1120px" width="22" height="56" viewBox="0 0 22 56"><path d="M2 2l18 26L2 54" stroke="#fff" stroke-width="2" fill="none" opacity=".8"/></svg>
  <div class="hero-caption">Thought Leadership &amp; Content Strategy</div>
  <div class="hero-dots"><i class="on"></i><i></i><i></i><i></i></div>
</section>

<section class="welcome">
  <h2 class="welcome-title">Welcome to <span>Brixholm Equity</span></h2>
  <p class="welcome-text">Lorem ipsum dolor sit amet, consectetuer adipiscing elit, sed diam nonummy nibh euismod tincidunt ut laoreet dolore magna aliquam erat volutpat. Ut wisi enim ad minim veniam, quis nostrud exerci tation ullamcorper suscipit lobortis nisl ut aliquip ex ea commodo consequat. Duis autem vel eum iriure dolor in hendrerit in vulputate velit esse molestie consequat, vel illum dolore eu feugiat nulla facilisis at vero eros et accumsan et iusto odio dignissim qui blandit praesent luptatum zzril delenit augue duis dolore te feugait nulla facilisi.</p>
  <a class="btn" style="left:98px;top:912px;width:103px;height:29px">Read More</a>
  <div class="video-frame">
    <div class="video-still" role="img" aria-label="Video still of a team meeting around a presentation screen"></div>
    <div class="play"><svg width="18" height="20" viewBox="0 0 18 20"><path d="M0 0l18 10L0 20z" fill="#1f5aa6"/></svg></div>
  </div>
</section>

<section class="who">
  <h2 class="section-title" style="top:36px">Who We <span>Are</span></h2>
  <div class="who-card" style="left:241px">
    <h3>Brixholm Equity Associates</h3>
    <p>Lorem ipsum dolor sit amet, consectetuer adipiscing elit, seddiam nonummy nibh euismod tincidunt ut laoreet</p>
    <span class="corner"></span><span class="corner-plus">+</span>
  </div>
  <div class="who-badge" style="left:161px"><div class="ring">
    <svg width="58" height="40" viewBox="0 0 58 40"><path d="M4 16l12-10 10 4 8-4 20 12-6 6-14-8-8 6-6-2M10 22l14 12 4-3 4 3 4-3 4 3 6-6" stroke="#222" stroke-width="3" fill="none" stroke-linejoin="round"/></svg>
  </div></div>
  <div class="who-card" style="left:706px">
    <h3>Our Missio</h3>
    <p>Lorem ipsum dolor sit amet, consectetuer adipiscing elit, seddiam nonummy nibh euismod tincidunt ut laoreet</p>
    <span class="corner"></span><span class="corner-plus">+</span>
  </div>
  <div class="who-badge" style="left:629px"><div class="ring">
    <svg width="54" height="54" viewBox="0 0 54 54"><circle cx="26" cy="28" r="22" fill="#222"/><circle cx="26" cy="28" r="15" fill="#fff"/><circle cx="26" cy="28" r="9" fill="#222"/><circle cx="26" cy="28" r="3.5" fill="#fff"/><path d="M26 28L48 6M42 4l6 2 2 6" stroke="#222" stroke-width="3" fill="none"/></svg>
  </div></div>
</section>

<section class="services">
  <h2 class="section-title" style="top:1392px">Our <span>Services</span></h2>
  <div class="service-card" style="left:98px"><div class="photo" role="img" aria-label="Hands joining puzzle pieces" style="background:linear-gradient(135deg,#3a5f8f,#c9b3a3 50%,#2d4e7a)"></div><h3>Company Set-up</h3></div>
  <div class="service-card" style="left:440px"><div class="photo" role="img" aria-label="Colleagues working together at a laptop" style="background:linear-gradient(135deg,#d9d6d2,#9a8a80 55%,#4a6c98)"></div><h3>Operational Support</h3></div>
  <div class="service-card" style="left:784px"><div class="photo" role="img" aria-label="Team standing in a glass meeting room" style="background:linear-gradient(180deg,#dfe7ef,#6d7886 60%,#c7ccd2)"></div><h3>Medtech Expertise</h3></div>
</section>

<section class="team">
  <h2 class="section-title" style="top:34px">Our <span>Services</span></h2>
  <div class="member" style="left:96px"><div class="photo" role="img" aria-label="Portrait of a team member in a suit" style="background:linear-gradient(180deg,#d8dde3,#7a7f88)"></div><h3>Marco Ventelli</h3><p>Marco Ventelli is a consultant for strategy development, marketing</p><span class="more"><svg width="12" height="8" viewBox="0 0 12 8"><path d="M1 7l5-5 5 5" stroke="#fff" stroke-width="2" fill="none"/></svg></span></div>
  <div class="member" style="left:354px"><div class="photo" role="img" aria-label="Portrait of a team member in business attire" style="background:linear-gradient(180deg,#a7c77e,#4e6b3a)"></div><h3>Sophie Darnell</h3><p>Marco Ventelli is a consultant for strategy development, marketing</p><span class="more"><svg width="12" height="8" viewBox="0 0 12 8"><path d="M1 7l5-5 5 5" stroke="#fff" stroke-width="2" fill="none"/></svg></span></div>
  <div class="member" style="left:612px"><div class="photo" role="img" aria-label="Portrait of a team member in a grey jacket" style="background:linear-gradient(180deg,#eef0f2,#9aa0a8)"></div><h3>Lena Morvaz</h3><p>Marco Ventelli is a consultant for strategy development, marketing</p><span class="more"><svg width="12" height="8" viewBox="0 0 12 8"><path d="M1 7l5-5 5 5" stroke="#fff" stroke-width="2" fill="none"/></svg></span></div>
  <div class="member" style="left:870px"><div class="photo" role="img" aria-label="Portrait of a team member holding a tablet" style="background:linear-gradient(180deg,#e6e3de,#5a6a88)"></div><h3>Marco Ventelli</h3><p>Marco Ventelli is a consultant for strategy development, marketing</p><span class="more"><svg width="12" height="8" viewBox="0 0 12 8"><path d="M1 7l5-5 5 5" stroke="#fff" stroke-width="2" fill="none"/></svg></span></div>
</section>
<svg class="team-arrow" style="left:52px" width="16" height="40" viewBox="0 0 16 40"><path d="M14 2L2 20l12 18" stroke="#c8c8c8" stroke-width="2" fill="none"/></svg>
<svg class="team-arrow" style="left:1124px" width="16" height="40" viewBox="0 0 16 40"><path d="M2 2l12 18L2 38" stroke="#c8c8c8" stroke-width="2" fill="none"/></svg>

<footer class="site-footer">
  <div class="footer-col" style="left:100px;width:135px">
    <h4>Quick Links</h4>
    <ul class="quick-links"><li>Home</li><li>Offering</li><li>Customers</li><li>Team</li><li>Contact Us</li></ul>
  </div>
  <div class="footer-col" style="left:284px;width:252px">
    <h4>Contact Information</h4>
    <div class="contact-line"><svg width="12" height="16" viewBox="0 0 12 16" style="flex:none;margin-top:3px"><path d="M6 0a6 6 0 016 6c0 4-6 10-6 10S0 10 0 6a6 6 0 016-6z" fill="#ddd"/><circle cx="6" cy="6" r="2.2" fill="#1e1e1e"/></svg><span>Brixholm Equity<br>Brixholm Equity Associates SA Rue des Tilleuls 14 2000 Neuchâtel,<br>Switzerland</span></div>
    <div class="contact-line" style="font-size:15px"><svg width="14" height="14" viewBox="0 0 24 24" style="flex:none;margin-top:4px"><path fill="#ddd" d="M6.6 10.8c1.4 2.8 3.8 5.1 6.6 6.6l2.2-2.2c.3-.3.7-.4 1-.2 1.1.4 2.3.6 3.6.6.6 0 1 .4 1 1V20c0 .6-.4 1-1 1C10.6 21 3 13.4 3 4c0-.6.4-1 1-1h3.5c.6 0 1 .4 1 1 0 1.3.2 2.5.6 3.6.1.3 0 .7-.2 1l-2.3 2.2z"/></svg><span>(123) 555 - 0190</span></div>
    <div class="contact-line"><svg width="13" height="10" viewBox="0 0 16 12" style="flex:none;margin-top:6px"><rect width="16" height="12" fill="#ddd"/><path d="M0 0l8 6 8-6" stroke="#1e1e1e" stroke-width="1.5" fill="none"/></svg><span>info@brixholm-equity.com</span></div>
  </div>
  <div class="footer-col" style="left:603px;width:258px">
    <h4>Quick Contact</h4>
    <div style="margin-top:8px">
      <div class="field">Name</div>
      <div class="field">Email</div>
      <div class="field big">Message</div>
      <a class="btn" style="position:relative;margin-top:6px;width:86px;height:28px">Submit</a>
    </div>
  </div>
  <div class="social" aria-label="Social links"><i></i><i></i><i></i><i></i></div>
</footer>
<div class="footer-bottom">Copyright 2016 Brixholm Equity. All Rights Reserved.</div>

</body>
</html>
```